Gutschein-Design zur Pflegeberatung
Zielgruppe
Wir feiern mit unserem Pflegedienst das 10 Jährige Jubiläum. Da es wegen der Corona Pandemie keine Feierlichkeiten geben kann, würde ich wir einen Gutschein für eine kostenlose Pflegeberatung erstellen lassen. Auf die Vorderseite bitte den Gutschein mit dem Text:
Bilder bitte aus den öffentlichen Portalen verwenden.
Gutschein zur Pflegeberatung
Wir unterstützen bei der Beantragung eines Pflegegrades und helfen bei abgelehnten Anträgen.
Gerne informieren wir Sie über umfangreiche Möglichkeiten der ambulante Pflege und erstellen einen individuellen Versorgungsplan. Darüber hinaus erhalte Sie praktische Tipps zu Alltagshilfen und konkrete Hilfestellungen rund um die Pflege, damit Sie noch so lange wie möglich zu
Hause bleiben können.
Unten bitte einfügen: Gutschein gültig bis einschließlich Juli 2022
Auf die Rückseite bitte eine kurze Info zu unserem 10 Jährigen bestehen.
Vielleicht vielleicht wieder mit dem Slogan, Seit 10 Jahren rund um die Uhr für Sie im Einsatz.
Aufgabenstellung
Da wir zwei ambulante Filialen betreiben, muss das Logo auf die zweite Filiale angepasst werden.
Der Text und die Informationen bleiben jedoch gleich. Der Gutschein sollte sofort auffallen und animieren, im Pflegedienst anzurufen.

```html
<!DOCTYPE html>
<html lang="de">
<head>
<meta charset="utf-8">
<title>Gutschein Pflegeberatung – Vitacura</title>
<link href="https://fonts.googleapis.com/css2?family=PT+Sans:ital,wght@0,400;1,400&family=Source+Sans+3:wght@400;600;700&display=swap" rel="stylesheet">
<style>
  :root {
    --green-light: #93c01f;
    --green-dark: #3aaa35;
    --orange: #f39200;
    --orange-light: #f8b133;
    --blue: #29a8e0;
    --brand-red: #b1191f;
    --ink: #1d1d1b;
    --white: #ffffff;
    --head-font: "PT Sans", sans-serif;
    --body-font: "Source Sans 3", sans-serif;
  }
  * { margin: 0; padding: 0; box-sizing: border-box; }
  html, body { width: 1200px; height: 2400px; overflow: hidden; background: var(--white); }
  h1, h2 { font-weight: 400; }
  .sheet {
    position: relative;
    width: 1280px; height: 2560px;
    transform: scale(0.9375);
    transform-origin: 0 0;
    font-family: var(--body-font);
    color: var(--ink);
  }
  .card { position: absolute; left: 160px; width: 953px; height: 477px; overflow: hidden; }

  /* Front */
  .voucher { background: var(--base); }
  .voucher--green { --top: var(--green-light); --base: var(--green-dark); }
  .voucher--orange { --top: var(--orange-light); --base: var(--blue); }
  .voucher__top { position: absolute; left: 0; top: 0; width: 100%; height: 246px; background: var(--top); }
  .voucher__title {
    position: absolute; left: 37px; top: 44px;
    font-family: var(--head-font); font-weight: 400; font-size: 64px; line-height: 1; color: var(--white);
  }
  .voucher__subtitle {
    position: absolute; left: 37px; top: 110px;
    font-family: var(--head-font); font-style: italic; font-size: 34px; line-height: 1; color: var(--white);
  }
  .brand {
    position: absolute; display: flex; align-items: center; gap: 10px;
    font-family: var(--body-font); font-weight: 700; color: var(--brand-red); letter-spacing: 1px;
  }
  .brand__mark { background: var(--brand-red); flex: none; }
  .voucher .brand { left: 650px; top: 48px; font-size: 36px; }
  .voucher .brand__mark { width: 44px; height: 44px; }
  .photo-row { position: absolute; display: flex; }
  .voucher .photo-row { left: 37px; top: 160px; width: 916px; height: 160px; }
  .photo { flex: 1; height: 100%; }
  .photo--couple-window { background: linear-gradient(100deg, #d9d2c8 0%, #f1eee6 45%, #c8d9b4 80%, #eef1e6 100%); }
  .photo--carer-hug { background: linear-gradient(100deg, #a8451a 0%, #c4622f 35%, #e7c7b4 60%, #d6701f 100%); }
  .photo--autumn-couple { background: linear-gradient(100deg, #6a7a2a 0%, #b5452a 35%, #d9b23a 55%, #5a6e7a 75%, #8a5a2a 100%); }
  .photo--bed-nurse { background: linear-gradient(100deg, #f2efec 0%, #e8c5b8 35%, #c79a5a 55%, #2a6fb8 80%, #e9e6e0 100%); }
  .photo--park-visit { background: linear-gradient(100deg, #7c9a4a 0%, #5a3a5e 40%, #cfc4b2 65%, #9ab06a 100%); }
  .voucher__text {
    position: absolute; top: 336px;
    font-size: 17.5px; line-height: 21px; color: var(--ink);
  }
  .voucher__text--left { left: 37px; width: 430px; }
  .voucher__text--right { left: 476px; width: 450px; }
  .voucher__validity {
    position: absolute; left: 476px; top: 441px;
    font-size: 17.5px; line-height: 21px; color: var(--white);
  }

  /* Back */
  .anniversary { background: var(--orange-light); }
  .anniversary--orange { --panel: var(--orange); }
  .anniversary--green { --panel: var(--green-light); }
  .anniversary__panel { position: absolute; left: 0; top: 0; width: 629px; height: 100%; background: var(--panel); }
  .anniversary__slogan {
    position: absolute; left: 37px; top: 30px;
    font-family: var(--head-font); font-weight: 400; font-style: italic; font-size: 44px; line-height: 52px; color: var(--white);
  }
  .anniversary .photo-row { left: 2px; top: 161px; width: 612px; height: 160px; }
  .anniversary__text {
    position: absolute; left: 39px; top: 333px; width: 560px;
    font-size: 17.5px; line-height: 21px;
  }
  .contact { position: absolute; left: 650px; top: 0; width: 300px; font-size: 15.5px; line-height: 19.3px; }
  .contact .brand { position: static; font-size: 24px; height: 70px; }
  .contact .brand__mark { width: 28px; height: 28px; }
  .brand--main { margin-top: 26px; }
  .brand--branch { margin-top: 14px; }
  .contact__label { font-weight: 700; margin-top: 6px; }
  .contact__kontakt { margin-top: 18px; }
  .contact__row { display: flex; }
  .contact__row span:first-child { width: 65px; }
  .contact__web {
    font-family: var(--head-font); font-style: italic; font-size: 31px; line-height: 1;
    color: var(--white); margin-top: 4px;
  }
</style>
</head>
<body>
<main class="sheet">

  <section class="card voucher voucher--green" style="top:99px">
    <div class="voucher__top"></div>
    <h1 class="voucher__title">Gutschein</h1>
    <p class="voucher__subtitle">zur kostenlosen Pflegeberatung</p>
    <div class="brand"><span class="brand__mark"></span>VITACURA</div>
    <div class="photo-row">
      <div class="photo photo--couple-window" role="img" aria-label="Foto: älteres Paar am Fenster"></div>
      <div class="photo photo--carer-hug" role="img" aria-label="Foto: Pflegerin umarmt lächelnde Seniorin"></div>
      <div class="photo photo--autumn-couple" role="img" aria-label="Foto: Seniorenpaar mit Herbstlaub im Garten"></div>
    </div>
    <p class="voucher__text voucher__text--left">Wir unterstützen bei der Beantragung eines Pflegegrades und helfen bei abgelehnten Anträgen.<br>Gerne informieren wir Sie über umfangreiche Möglichkei-ten der ambulante Pflege und erstellen einen individuel-len Versorgungsplan.</p>
    <p class="voucher__text voucher__text--right">Darüber hinaus erhalte Sie praktische Tipps zu Alltagshilfen und konkrete Hilfestellungen rund um die Pflege, damit Sie noch so lange wie möglich zu<br>Hause bleiben können.</p>
    <p class="voucher__validity">Gutschein gültig bis einschließlich Juli 2022</p>
  </section>

  <section class="card anniversary anniversary--orange" style="top:624px">
    <div class="anniversary__panel"></div>
    <h2 class="anniversary__slogan">Seit 10 Jahren rund um die Uhr<br>für Sie im Einsatz.</h2>
    <div class="photo-row">
      <div class="photo photo--bed-nurse" role="img" aria-label="Foto: Seniorin im Bett mit Pflegerin"></div>
      <div class="photo photo--park-visit" role="img" aria-label="Foto: Seniorin und junge Frau im Park"></div>
    </div>
    <p class="anniversary__text">Auf die Rückseite bitte eine kurze Info zu unserem 10 Jährigen bestehen. Lorem ipsum dolor sit amet, consectetuer adipiscing elit, sed diam no-nummy nibh euismod tincidunt ut laoreet dolore magna aliquam erat vo-lutpat. Ut wisi enim ad minim veniam, quis nostrud exerci tation ullamcor-per suscipit lobortis nisl ut aliquip ex ea commodo consequat.</p>
    <div class="contact">
      <div class="brand brand--main"><span class="brand__mark"></span>VITACURA</div>
      <p class="contact__label">Vitacura Ambulante Pflege GmbH</p>
      <p>Lindenweg 12<br>23966 Birkenfelde<br>Tel. 03841- 40512876</p>
      <div class="brand brand--branch"><span class="brand__mark"></span>VITACURA</div>
      <p class="contact__label">Niederlassung in Wiesenau:</p>
      <p>Am Marktplatz 7<br>17248 Wiesenau<br>Tel. 038294 208815</p>
      <p class="contact__label contact__kontakt">Kontakt:</p>
      <p class="contact__row"><span>Telefon:</span><span>+49 (0) 38294 / 208815</span></p>
      <p class="contact__row"><span>E-Mail:</span><span>info@vitacura.de</span></p>
      <p class="contact__web">www.Vitacura.de</p>
    </div>
  </section>

  <section class="card voucher voucher--orange" style="top:1320px">
    <div class="voucher__top"></div>
    <h1 class="voucher__title">Gutschein</h1>
    <p class="voucher__subtitle">zur kostenlosen Pflegeberatung</p>
    <div class="brand"><span class="brand__mark"></span>VITACURA</div>
    <div class="photo-row">
      <div class="photo photo--couple-window" role="img" aria-label="Foto: älteres Paar am Fenster"></div>
      <div class="photo photo--carer-hug" role="img" aria-label="Foto: Pflegerin umarmt lächelnde Seniorin"></div>
      <div class="photo photo--autumn-couple" role="img" aria-label="Foto: Seniorenpaar mit Herbstlaub im Garten"></div>
    </div>
    <p class="voucher__text voucher__text--left">Wir unterstützen bei der Beantragung eines Pflegegrades und helfen bei abgelehnten Anträgen.<br>Gerne informieren wir Sie über umfangreiche Möglichkei-ten der ambulante Pflege und erstellen einen individuel-len Versorgungsplan.</p>
    <p class="voucher__text voucher__text--right">Darüber hinaus erhalte Sie praktische Tipps zu Alltagshilfen und konkrete Hilfestellungen rund um die Pflege, damit Sie noch so lange wie möglich zu<br>Hause bleiben können.</p>
    <p class="voucher__validity">Gutschein gültig bis einschließlich Juli 2022</p>
  </section>

  <section class="card anniversary anniversary--green" style="top:1845px">
    <div class="anniversary__panel"></div>
    <h2 class="anniversary__slogan">Seit 10 Jahren rund um die Uhr<br>für Sie im Einsatz.</h2>
    <div class="photo-row">
      <div class="photo photo--bed-nurse" role="img" aria-label="Foto: Seniorin im Bett mit Pflegerin"></div>
      <div class="photo photo--park-visit" role="img" aria-label="Foto: Seniorin und junge Frau im Park"></div>
    </div>
    <p class="anniversary__text">Auf die Rückseite bitte eine kurze Info zu unserem 10 Jährigen bestehen. Lorem ipsum dolor sit amet, consectetuer adipiscing elit, sed diam no-nummy nibh euismod tincidunt ut laoreet dolore magna aliquam erat vo-lutpat. Ut wisi enim ad minim veniam, quis nostrud exerci tation ullamcor-per suscipit lobortis nisl ut aliquip ex ea commodo consequat.</p>
    <div class="contact">
      <div class="brand brand--main"><span class="brand__mark"></span>VITACURA</div>
      <p class="contact__label">Vitacura Ambulante Pflege GmbH</p>
      <p>Lindenweg 12<br>23966 Birkenfelde<br>Tel. 03841- 40512876</p>
      <div class="brand brand--branch"><span class="brand__mark"></span>VITACURA</div>
      <p class="contact__label">Niederlassung in Wiesenau:</p>
      <p>Am Marktplatz 7<br>17248 Wiesenau<br>Tel. 038294 208815</p>
      <p class="contact__label contact__kontakt">Kontakt:</p>
      <p class="contact__row"><span>Telefon:</span><span>+49 (0) 38294 / 208815</span></p>
      <p class="contact__row"><span>E-Mail:</span><span>info@vitacura.de</span></p>
      <p class="contact__web">www.Vitacura.de</p>
    </div>
  </section>

</main>
</body>
</html>
```